The Lantern and the Meadow: A Quiet Bloom Within Us

We need a book cover/spine and back cover for a multi author book called the Lantern and The Meadow: A Quiet Bloom Within Us. This will be a collection of stories from women who major transformational stories to tell. They embark on a voyage, find themselves in uncharted territory, find friends or allies and in the end find themselves back home to themselves. I want this book cover to feel fun of wonder, adventure, intrigue with a a dainty energy. I have uploaded some images for inspiration but not to use in the design because they are not images I have permission to use.

```html
<!DOCTYPE html>
<html lang="en">
<head>
<meta charset="utf-8">
<title>The Lantern and the Meadow: A Quiet Bloom Within Us</title>
<link rel="stylesheet" href="https://fonts.googleapis.com/css2?family=Montserrat:wght@700;800&family=Kaushan+Script&family=Roboto+Condensed:wght@400&display=swap">
<style>
  :root {
    --stage: #8a8a8a;
    --stage-light: #a8a8a8;
    --cover: #a0577e;
    --cover-deep: #8c4a6e;
    --gold: #f6a935;
    --white: #ffffff;
    --accent-yellow: #f4ea1c;
    --bloom-violet: #8a4fc4;
    --bloom-blue: #6f7ee0;
    --bloom-lilac: #b89ae6;
  }
  * { margin: 0; padding: 0; box-sizing: border-box; }
  html, body { width: 1200px; height: 1200px; overflow: hidden; }
  body {
    background: radial-gradient(circle at 30% 35%, var(--stage-light), var(--stage) 70%);
    display: flex; align-items: center; justify-content: center;
  }
  .cover {
    position: relative;
    width: 760px; height: 1120px;
    background: var(--cover);
    overflow: hidden;
    box-shadow: 0 20px 50px rgba(0,0,0,.35);
  }
  .title { position: absolute; top: 40px; left: 0; right: 0; text-align: center; }
  .title-small {
    display: flex; align-items: center; justify-content: center; gap: 18px;
    font-family: "Montserrat", sans-serif; font-weight: 800;
    color: var(--gold); font-size: 58px; letter-spacing: -1px; line-height: 1;
  }
  .title-small .rule { height: 3px; width: 190px; background: var(--gold); }
  .title-main {
    font-family: "Montserrat", sans-serif; font-weight: 800;
    color: var(--white); font-size: 118px; line-height: 1; letter-spacing: -2px;
    margin: 14px 0 16px;
  }
  .title-script {
    font-family: "Kaushan Script", cursive;
    color: var(--white); font-size: 170px; line-height: 1; margin-top: 4px;
  }
  .meadow-photo {
    position: absolute; left: 0; right: 0; top: 470px; height: 500px;
    background:
      linear-gradient(to bottom, var(--cover) 0%, rgba(160,87,126,0) 22%),
      radial-gradient(ellipse at 35% 70%, var(--bloom-violet), transparent 60%),
      radial-gradient(ellipse at 80% 55%, var(--bloom-blue), transparent 60%),
      linear-gradient(160deg, var(--bloom-lilac), var(--bloom-violet) 55%, var(--bloom-blue));
  }
  .subtitle {
    position: absolute; left: 110px; top: 650px;
    background: rgba(160,87,126,.88);
    padding: 14px 18px;
    font-family: "Roboto Condensed", sans-serif; font-weight: 400;
    font-size: 42px; line-height: 1.08; color: var(--white);
  }
  .subtitle .highlight { color: var(--accent-yellow); }
  .author-band {
    position: absolute; left: 0; right: 0; bottom: 0; height: 150px;
    background: var(--cover);
    border-top: 6px solid var(--gold);
    display: flex; align-items: center; justify-content: center;
  }
  .author-name {
    font-family: "Montserrat", sans-serif; font-weight: 700;
    color: var(--white); font-size: 62px; letter-spacing: 22px; padding-left: 22px;
  }
</style>
</head>
<body>
  <main class="cover">
    <div class="meadow-photo" role="img" aria-label="Photograph of a woman in a white dress and straw hat walking along a path through a field of purple and blue flowers"></div>
    <header class="title">
      <div class="title-small"><span class="rule"></span>THE<span class="rule"></span></div>
      <h1 class="title-main">LANTERN</h1>
      <div class="title-small"><span class="rule"></span>AND THE<span class="rule"></span></div>
      <div class="title-script">Meadow</div>
    </header>
    <p class="subtitle">A Quiet Bloom<br><span class="highlight">Within Us</span></p>
    <footer class="author-band"><span class="author-name">AUTHOR</span></footer>
  </main>
</body>
</html>
```